business card for LWR pty ltd

We require a business card that stands out . I have included our company flyer and would like the services listed to be put on the card so when we Give out the cards to customers they have an idea of services we provide. need the winning design to be in editable photo shop format, editable iMac pages format or editable windows publisher format, so that I can enter in names, email addresses, phone numbers etc myself. I have included a pdf documents of info / items needed on the card to use as reference please.
Updates

need more submissions

Need extra days to review

Sick

Target Market(s)

new customers

Contact Information for Business Card

details are on attached business card requirements file

Requirements
Must have
• I have attached a list of must haves

```html
<!DOCTYPE html>
<html lang="en">
<head>
<meta charset="utf-8">
<title>LWR pty ltd – Business Card</title>
<link href="https://fonts.googleapis.com/css2?family=Roboto:wght@400;500;700&display=swap" rel="stylesheet">
<style>
  :root {
    --gold: #a07434;
    --gold-band: #8f6630;
    --gold-deep: #94692f;
    --ink: #050505;
    --steel-dark: #111214;
    --steel-mid: #2a2c30;
    --chrome: #c9ccd1;
    --white: #ffffff;
  }
  * { box-sizing: border-box; margin: 0; padding: 0; }
  html, body { width: 1141px; height: 1200px; overflow: hidden; background: var(--white); }
  body { position: relative; font-family: "Roboto", Arial, sans-serif; color: var(--white); }

  .card {
    position: absolute; left: 136px; width: 850px; height: 485px;
    border-radius: 26px; overflow: hidden;
  }
  .card--front { top: 87px; background: var(--gold-deep); }
  .card--back { top: 614px; background: var(--ink); }

  /* front */
  .front__hero {
    position: absolute; left: 0; top: 0; width: 100%; height: 291px;
    background: radial-gradient(ellipse at 50% 45%, var(--steel-mid) 0%, var(--steel-dark) 55%, #050506 100%);
  }
  .front__band {
    position: absolute; left: 0; top: 291px; width: 100%; height: 14px;
    background: var(--gold-band);
  }
  .brand-name {
    position: absolute; left: 0; top: 75px; width: 100%;
    text-align: center; font-weight: 700; font-size: 132px; letter-spacing: 4px;
    color: var(--chrome); line-height: 1;
  }
  .services {
    position: absolute; top: 330px; list-style: none;
    font-weight: 500; font-size: 16px; line-height: 22px;
  }
  .services--left { left: 175px; }
  .services--right { left: 496px; }
  .services li { position: relative; padding-left: 25px; }
  .services li svg { position: absolute; left: 0; top: 4px; width: 14px; height: 14px; }

  /* back */
  .back__panel {
    position: absolute; left: 0; top: 0; width: 401px; height: 100%;
    background: var(--gold);
  }
  .back__company { position: absolute; left: 53px; top: 124px; font-size: 26px; font-weight: 700; }
  .back__person { position: absolute; left: 53px; top: 162px; font-size: 25px; font-weight: 700; }
  .back__rule { position: absolute; left: 53px; top: 205px; width: 276px; height: 2px; background: var(--white); }
  .contacts { position: absolute; left: 53px; top: 226px; list-style: none; font-size: 15px; }
  .contacts li { position: relative; height: 27px; line-height: 20px; padding-left: 26px; }
  .contacts li svg { position: absolute; left: 2px; top: 3px; width: 14px; height: 14px; }
  .back__photo {
    position: absolute; left: 346px; top: 196px; width: 504px; height: 235px;
    background: linear-gradient(100deg, #2a241c 0%, #4a3a22 45%, #6d5a2a 70%, #3a332a 100%);
    border-radius: 4px;
  }
</style>
</head>
<body>

<section class="card card--front">
  <div class="front__hero" role="img" aria-label="Dark perforated metal mesh background"></div>
  <div class="brand-name">LWR</div>
  <div class="front__band"></div>

  <ul class="services services--left">
    <li><svg viewBox="0 0 14 14"><circle cx="7" cy="7" r="7" fill="#fff"/><path d="M3.8 7.2l2.2 2.2 4.2-4.4" stroke="#94692f" stroke-width="1.8" fill="none"/></svg>Over size loads/Hot Shot Loads</li>
    <li><svg viewBox="0 0 14 14"><circle cx="7" cy="7" r="7" fill="#fff"/><path d="M3.8 7.2l2.2 2.2 4.2-4.4" stroke="#94692f" stroke-width="1.8" fill="none"/></svg>Heavy Vehicle Recovery services</li>
    <li><svg viewBox="0 0 14 14"><circle cx="7" cy="7" r="7" fill="#fff"/><path d="M3.8 7.2l2.2 2.2 4.2-4.4" stroke="#94692f" stroke-width="1.8" fill="none"/></svg>Potable Water Deliveries</li>
    <li><svg viewBox="0 0 14 14"><circle cx="7" cy="7" r="7" fill="#fff"/><path d="M3.8 7.2l2.2 2.2 4.2-4.4" stroke="#94692f" stroke-width="1.8" fill="none"/></svg>Road Building/Maintenance</li>
    <li><svg viewBox="0 0 14 14"><circle cx="7" cy="7" r="7" fill="#fff"/><path d="M3.8 7.2l2.2 2.2 4.2-4.4" stroke="#94692f" stroke-width="1.8" fill="none"/></svg>Earthworks</li>
    <li><svg viewBox="0 0 14 14"><circle cx="7" cy="7" r="7" fill="#fff"/><path d="M3.8 7.2l2.2 2.2 4.2-4.4" stroke="#94692f" stroke-width="1.8" fill="none"/></svg>Sand &amp; Metal Supply &amp; Cartage</li>
  </ul>

  <ul class="services services--right">
    <li><svg viewBox="0 0 14 14"><circle cx="7" cy="7" r="7" fill="#fff"/><path d="M3.8 7.2l2.2 2.2 4.2-4.4" stroke="#94692f" stroke-width="1.8" fill="none"/></svg>Road Train Tippers</li>
    <li><svg viewBox="0 0 14 14"><circle cx="7" cy="7" r="7" fill="#fff"/><path d="M3.8 7.2l2.2 2.2 4.2-4.4" stroke="#94692f" stroke-width="1.8" fill="none"/></svg>Road Train Tankers</li>
    <li><svg viewBox="0 0 14 14"><circle cx="7" cy="7" r="7" fill="#fff"/><path d="M3.8 7.2l2.2 2.2 4.2-4.4" stroke="#94692f" stroke-width="1.8" fill="none"/></svg>Road Train Flat Tops</li>
    <li><svg viewBox="0 0 14 14"><circle cx="7" cy="7" r="7" fill="#fff"/><path d="M3.8 7.2l2.2 2.2 4.2-4.4" stroke="#94692f" stroke-width="1.8" fill="none"/></svg>Drop Deck Trailers</li>
    <li><svg viewBox="0 0 14 14"><circle cx="7" cy="7" r="7" fill="#fff"/><path d="M3.8 7.2l2.2 2.2 4.2-4.4" stroke="#94692f" stroke-width="1.8" fill="none"/></svg>Mine site accredited<br>equipment &amp; Operators</li>
  </ul>
</section>

<section class="card card--back">
  <div class="back__photo" role="img" aria-label="Photo of a road train truck carrying a grader on a drop deck trailer"></div>
  <div class="back__panel">
    <h1 class="back__company">LWR Pty Ltd</h1>
    <h2 class="back__person">DANIEL HARPER (Director)</h2>
    <div class="back__rule"></div>
    <ul class="contacts">
      <li><svg viewBox="0 0 14 14"><path d="M7 0.5a4.5 4.5 0 0 0-4.5 4.5c0 3.4 4.5 8.5 4.5 8.5s4.5-5.1 4.5-8.5A4.5 4.5 0 0 0 7 0.5z" fill="#fff"/><circle cx="7" cy="5" r="1.7" fill="#a07434"/></svg>Depot: Lot 444 example address Australia</li>
      <li><svg viewBox="0 0 14 14"><rect x="0.5" y="3" width="13" height="9" fill="#fff"/><path d="M0.5 3.5l6.5 4.5 6.5-4.5" stroke="#a07434" stroke-width="1.2" fill="none"/></svg>Email: email@redrockhaulage.com.au</li>
      <li><svg viewBox="0 0 14 14"><path d="M3 0.8l2.2 2.8-1.2 1.6c0.9 1.9 2.3 3.3 4.2 4.2l1.6-1.2 2.8 2.2-1.4 2.4C6 12.4 1.6 8 1.2 2.2z" fill="#fff"/></svg>Phone: 000 444 000</li>
      <li><svg viewBox="0 0 14 14"><circle cx="7" cy="7" r="6.5" fill="#fff"/><path d="M4 3.5c1.5 0.5 2 2 1 3s0.5 2.5 2 2.5M9.5 2.5c-0.5 1.5 0.5 2.5 2 2.5M8.5 12c0-1.5 1-2.5 2.5-3" stroke="#a07434" stroke-width="1.3" fill="none"/></svg>Website: www.websiteaddress.com</li>
    </ul>
  </div>
</section>

</body>
</html>
```